Brimcraft sales

🎨 Project Title:
Brimcraft Designer Web Page for WooCommerce (French Texts Provided) i show you exemple what i need

📄 Project Description:
We are looking to create a web page design (desktop and mobile) for a custom cap ordering experience. This page will be integrated into our existing WooCommerce transactional site. The goal is to allow customers to configure and order personalized caps easily and visually.

The entire interface will ultimately be in French, but you can design using placeholder texts (we will provide the actual French text later).

💡 Page Goals & Features:
The page should be modern, clean, and conversion-oriented, and include the following features:

Header area:

Visually showcase examples of designed caps (carousel or grid layout)

A clear title and short description

Customization Steps (in order):

Material selection: users choose the type of material for the cap

Cap color: users choose the base color of the cap

Patch shape: users select the shape of the patch (e.g., round, square, rectangle, custom)

Patch location: mainly the front, but possibly add other options

Quantity selection: users choose how many units they want (with price updates)

Price display: show price per unit and total cost depending on quantity

Call to Action (CTA):

Add to cart or request a quote button

Smooth integration with WooCommerce logic (cart, checkout, etc.)

Other Optional Sections:

FAQ

Delivery timeline

Client testimonials or reviews

🛠 Technical Notes:
The design must be compatible with WooCommerce

Responsive design for both desktop and mobile

The final output can be delivered in Figma, Adobe XD, or layered PSD (no coding required for now)

We will handle the French translation; just use placeholder text where needed

🖼 Inspiration / Style:
Clean and modern layout

Easy to navigate

Visual configurator-style approach (like t-shirt or shoe customization sites)

Feel free to use mockups of caps to enhance the presentation

📎 What we will provide:
Actual French text

Product images (caps, patch styles, color swatches)

Brand logo and colors

Optional references if needed

✅ Deliverables:
Homepage (or dedicated product page) layout

Mobile and desktop views

Editable design file (Figma, XD, PSD)

i need very nice 1 or 2 hat design to present to customer design un der the hat and front and see coupple of shape of the patche to show option possible

```html
<!DOCTYPE html>
<html lang="en">
<head>
<meta charset="utf-8">
<title>Brimcraft – Design Your Custom Cap</title>
<link href="https://fonts.googleapis.com/css2?family=Playfair+Display:ital,wght@0,600;0,700;0,800;0,900;1,700;1,800;1,900&family=Montserrat:ital,wght@0,400;0,500;0,600;1,400;1,500&display=swap" rel="stylesheet">
<style>
:root{
  --pink:#d9418d;
  --gold:#c19b48;
  --ink:#1f1a17;
  --muted:#6b625c;
  --blush:#fbe9ed;
  --sand:#f1e9da;
  --salmon:#e8ad98;
  --line:#e3a6c4;
  --white:#ffffff;
}
*{box-sizing:border-box;margin:0;padding:0}
html,body{width:1200px;height:3983px;overflow:hidden;background:var(--white)}
body{font-family:'Montserrat',sans-serif;color:var(--ink);position:relative}
.serif{font-family:'Playfair Display',serif}
.abs{position:absolute}
section,header,footer{position:absolute;left:0;width:1200px}

/* header */
.site-header{top:0;height:71px;background:var(--white)}
.brand{left:111px;top:20px;font-family:'Playfair Display',serif;font-weight:800;font-size:27px;color:var(--ink)}
.nav a{position:absolute;top:28px;font-family:'Playfair Display',serif;font-weight:700;font-size:15px;color:var(--ink);text-decoration:none}
.nav a.active{color:var(--gold)}
.header-icon{position:absolute;top:25px;width:28px;height:28px;border-radius:50%;background:var(--pink)}
.header-icon svg{position:absolute;left:7px;top:7px}

/* hero */
.hero{top:71px;height:603px;overflow:hidden;background:linear-gradient(180deg,#dfe9ee 0%,#cfe0e4 38%,#c8d6d4 52%,#e6ddd0 70%,#d9cbb8 100%)}
.hero-sun{left:510px;top:6px;width:588px;height:588px;border-radius:50%;background:linear-gradient(160deg,#fbc95a 0%,#f7b27a 45%,#f1a3ae 100%)}
.hero-hats{left:420px;top:16px;width:720px;height:560px;border-radius:48% 52% 45% 55%;background:radial-gradient(ellipse at 50% 50%,#d8b47e 0%,#c49a63 60%,rgba(196,154,99,0) 72%)}
.hero h1{left:70px;top:178px;font-family:'Playfair Display',serif;font-style:italic;font-weight:900;font-size:56px;line-height:51px;color:var(--pink)}
.hero p{left:68px;top:305px;font-size:20px;line-height:29px;color:var(--ink)}
.btn-gold{left:70px;top:390px;width:173px;height:52px;border-radius:26px;background:var(--gold);color:var(--white);font-family:'Playfair Display',serif;font-weight:800;font-size:16px;display:flex;align-items:center;justify-content:center}
.dot{position:absolute;top:577px;width:14px;height:14px;border-radius:50%;border:1.5px solid #ffffff}
.dot.on{background:var(--pink);border-color:var(--pink)}

/* section titles */
.section-title{left:0;width:1200px;text-align:center;font-family:'Playfair Display',serif;font-weight:800;font-size:48px;line-height:60px}
.t-gold{color:var(--gold)}
.t-pink{color:var(--pink)}
.t-italic{font-style:italic;font-weight:900}
.title-rule{left:572px;width:56px;height:3px;background:var(--pink)}

/* products */
.products{top:674px;height:834px}
.thumb{position:absolute;left:66px;width:73px;height:70px}
.thumb.selected{border:4px solid var(--pink);background:#fff}
.thumb.selected .fill{position:absolute;inset:4px;background:linear-gradient(135deg,#f3e2b8,#e8c98a)}
.straw{background:linear-gradient(135deg,#c9a26b,#8f6a3f)}
.pinkhat{background:linear-gradient(135deg,#e0569a,#d9a36a)}
.stage{left:151px;top:219px;width:420px;height:514px;border:6px solid var(--pink);background:#fff}
.stage .fill{position:absolute;left:20px;top:110px;width:370px;height:250px;border-radius:40%;background:radial-gradient(ellipse at 40% 60%,#d9b57c 0%,#e6c84a 55%,rgba(255,255,255,0) 72%)}
.pname{left:594px;top:210px;font-family:'Playfair Display',serif;font-weight:800;font-size:32px}
.pdesc{left:594px;top:258px;width:220px;font-size:10.5px;line-height:16px;color:var(--muted)}
.price{left:594px;top:296px;font-family:'Playfair Display',serif;font-weight:700;font-size:28px;color:var(--pink)}
.price s{color:#b7a58c;margin-left:12px}
.stars{display:flex;gap:3px}
.reviews{left:594px;top:381px;font-size:11px;color:var(--ink)}
.vrule{left:824px;top:215px;width:1px;height:178px;background:var(--line)}
.hrule{left:594px;top:408px;width:507px;height:1px;background:var(--pink)}
.label{position:absolute;font-size:17px;font-weight:500;color:var(--ink)}
.mat{position:absolute;top:247px;width:46px;height:46px}
.mat.selected{outline:2px solid var(--ink);outline-offset:1px}
.swatch{position:absolute;top:349px;width:28px;height:28px}
.swatch.selected{outline:2px solid var(--ink);outline-offset:1px}
.shape-img{position:absolute;top:428px;height:46px}
.shape-label{position:absolute;top:480px;font-size:11px;color:var(--muted);text-align:center}
.loc{position:absolute;top:518px;height:37px;border:1px solid #e0d6d0;background:#fff;font-size:11.5px;color:var(--muted);display:flex;align-items:center;justify-content:center}
.loc.on{background:var(--pink);border-color:var(--pink);color:#fff;font-weight:600}
.qty{left:750px;top:584px;width:142px;height:38px;border:1px solid #e0d6d0;background:#fff}
.qty span.v{position:absolute;left:32px;top:10px;font-size:12px;color:var(--muted)}
.qbtn{position:absolute;top:6px;width:26px;height:26px;background:var(--pink);color:#fff;font-size:16px;display:flex;align-items:center;justify-content:center}
.tiers{left:904px;top:584px;width:172px;height:38px;border:1px solid #e0d6d0;background:#fff;font-family:'Playfair Display',serif;font-size:9px;display:flex;align-items:center;justify-content:center;gap:4px;color:var(--ink)}
.btn-pink{border-radius:28px;background:var(--pink);color:#fff;font-family:'Playfair Display',serif;font-weight:800;display:flex;align-items:center;justify-content:center;box-shadow:0 3px 8px rgba(217,65,141,.25)}

/* faq */
.faq{top:1508px;height:592px;background:var(--blush)}
.faq-q{position:absolute;left:269px;font-family:'Playfair Display',serif;font-weight:700;font-size:17px;color:var(--gold)}
.faq-a{left:269px;top:210px;width:570px;font-size:17.5px;line-height:27px;color:var(--ink)}
.faq-toggle{position:absolute;left:912px;width:17px;height:17px;border-radius:50%;background:var(--pink)}
.faq-toggle svg{position:absolute;left:4px;top:4px}

/* delivery */
.delivery{top:2100px;height:552px}
.step-head{position:absolute;width:260px;text-align:center;font-family:'Playfair Display',serif;font-weight:700;font-size:17px;color:var(--ink)}
.step-time{position:absolute;width:260px;text-align:center;font-family:'Playfair Display',serif;font-weight:600;font-size:20px;color:var(--gold)}
.step-art{position:absolute;top:242px;height:132px;border-radius:10px}
.step-name{position:absolute;width:260px;text-align:center;font-family:'Playfair Display',serif;font-weight:700;font-size:20px}

/* testimonials */
.reviews-sec{top:2652px;height:641px;background:var(--sand)}
.card{position:absolute;top:205px;width:314px;height:274px;background:var(--blush)}
.card h3{position:absolute;left:28px;top:26px;font-family:'Playfair Display',serif;font-weight:700;font-size:20px}
.card .stars{position:absolute;left:28px;top:62px}
.card .q{position:absolute;right:24px;top:4px;font-family:'Playfair Display',serif;font-weight:900;font-size:72px;line-height:72px;color:#e6c6d2}
.card p{position:absolute;left:28px;top:101px;width:250px;font-size:12.5px;line-height:19.5px;font-style:italic;color:#5a514b}
.rdot{position:absolute;top:538px;width:14px;height:14px;border-radius:50%;border:1.5px solid var(--pink)}
.rdot.on{background:var(--pink)}

/* newsletter */
.newsletter{top:3293px;height:302px}
.nl-sub{left:0;width:1200px;top:135px;text-align:center;font-size:17px;color:var(--ink)}
.nl-input{left:326px;top:179px;width:381px;height:41px;border-radius:21px;background:#fff;box-shadow:0 2px 10px rgba(0,0,0,.12);font-size:12px;color:var(--muted);display:flex;align-items:center;padding-left:28px;gap:10px}

/* footer */
.site-footer{top:3595px;height:388px;background:var(--salmon)}
.f-brand{left:130px;top:132px;font-family:'Playfair Display',serif;font-weight:800;font-size:36px;color:var(--pink)}
.social{position:absolute;top:219px;width:38px;height:38px;border-radius:50%;background:#fff}
.f-head{position:absolute;top:74px;font-family:'Playfair Display',serif;font-weight:700;font-size:17px;color:var(--ink)}
.f-link{position:absolute;left:380px;font-size:15px;color:var(--ink)}
.f-contact{position:absolute;left:589px;font-size:15px;line-height:31px;color:var(--ink)}
.f-icon{position:absolute;left:562px}
.f-note{left:858px;top:117px;width:220px;font-size:13px;line-height:25px;color:var(--ink)}
.f-input{left:858px;top:182px;width:215px;height:42px;background:#fff;font-size:13px;color:var(--muted);padding:13px 0 0 10px}
.f-send{left:1025px;top:182px;width:48px;height:42px;background:var(--pink)}
.f-rule{left:111px;top:312px;width:977px;height:1px;background:#9c6a5c}
.copyright{left:0;width:1200px;top:337px;text-align:center;font-size:13.5px;color:var(--ink)}
</style>
</head>
<body>

<header class="site-header">
  <div class="abs brand">Brimcraft</div>
  <nav class="nav">
    <a class="active" style="left:532px">Home</a>
    <a style="left:604px">About Us</a>
    <a style="left:697px">Shop</a>
    <a style="left:762px">FAQ</a>
    <a style="left:822px">Reviews</a>
  </nav>
  <div class="header-icon" style="left:966px"><svg width="14" height="14" viewBox="0 0 14 14"><circle cx="7" cy="4.5" r="3" fill="#fff"/><path d="M1.5 13c0-3 2.5-5 5.5-5s5.5 2 5.5 5z" fill="#fff"/></svg></div>
  <div class="header-icon" style="left:1003px"><svg width="14" height="14" viewBox="0 0 14 14"><path d="M7 12.5 1.6 7.2A3.2 3.2 0 0 1 7 2.9a3.2 3.2 0 0 1 5.4 4.3z" fill="#fff"/></svg></div>
  <div class="header-icon" style="left:1040px"><svg width="14" height="14" viewBox="0 0 14 14" fill="none" stroke="#fff" stroke-width="1.4"><path d="M1 2h2l1.6 7h7l1.4-5H4"/><circle cx="5.5" cy="12" r="1"/><circle cx="10.5" cy="12" r="1"/></svg></div>
  <div class="abs" style="left:1058px;top:22px;width:10px;height:10px;border-radius:50%;background:#1f1a17;color:#fff;font-size:7px;text-align:center;line-height:10px">0</div>
</header>

<section class="hero" role="img" aria-label="Beach scene backdrop with sea and sand">
  <div class="abs hero-sun"></div>
  <div class="abs hero-hats" role="img" aria-label="Two woven straw hats with colourful front patches"></div>
  <h1 class="abs">Design Your<br>Custom Cap</h1>
  <p class="abs">Personalize your cap in just<br>a few easy steps.</p>
  <div class="abs btn-gold">SHOP NOW</div>
  <span class="dot" style="left:100px"></span>
  <span class="dot" style="left:123px"></span>
  <span class="dot on" style="left:145px"></span>
  <span class="dot" style="left:168px"></span>
</section>

<section class="products">
  <h2 class="abs section-title" style="top:100px"><span class="t-gold">Our</span> <span class="t-pink">Products</span></h2>
  <div class="abs title-rule" style="top:174px"></div>

  <div class="thumb selected" style="top:219px"><div class="fill" role="img" aria-label="Straw hat with round patch"></div></div>
  <div class="thumb straw" style="top:294px" role="img" aria-label="Straw weave detail"></div>
  <div class="thumb pinkhat" style="top:368px" role="img" aria-label="Straw hat on pink backdrop"></div>
  <div class="thumb straw" style="top:442px" role="img" aria-label="Brim edge detail"></div>
  <div class="thumb pinkhat" style="top:516px" role="img" aria-label="Straw hat on pink backdrop, front view"></div>
  <div class="thumb straw" style="top:591px" role="img" aria-label="Straw weave close-up"></div>
  <div class="thumb straw" style="top:665px" role="img" aria-label="Hat band detail"></div>

  <div class="abs stage"><div class="fill" role="img" aria-label="Straw hat with yellow brim and a round patch shown front and under the brim"></div></div>

  <div class="abs pname">Ksaeicn Hat</div>
  <div class="abs pdesc">Faerspiciatis unde omnis iste natus error csesit volupt atem.</div>
  <div class="abs price">$ 12.00<s>$ 15.00</s></div>
  <div class="abs stars" style="left:594px;top:353px">
    <svg width="100" height="18" viewBox="0 0 100 18" fill="#c19b48"><g id="s"><path d="M9 1l2.4 5.2 5.6.6-4.2 3.8 1.2 5.6L9 13.4 4 16.2l1.2-5.6L1 6.8l5.6-.6z"/></g><use href="#s" x="20"/><use href="#s" x="40"/><use href="#s" x="60"/><use href="#s" x="80"/></svg>
  </div>
  <div class="abs reviews">189 Customers Review</div>
  <div class="abs vrule"></div>

  <div class="label" style="left:858px;top:214px">Material</div>
  <div class="mat straw" style="left:860px" role="img" aria-label="Natural straw"></div>
  <div class="mat selected" style="left:920px;background:linear-gradient(135deg,#b58c55,#7a5a34)" role="img" aria-label="Dark straw"></div>
  <div class="mat" style="left:980px;background:linear-gradient(135deg,#d4b684,#9e7d4e)" role="img" aria-label="Light straw"></div>
  <div class="mat" style="left:1040px;background:linear-gradient(135deg,#c8a774,#8c6c40)" role="img" aria-label="Fine straw"></div>

  <div class="label" style="left:858px;top:316px">Color</div>
  <div class="swatch" style="left:860px;background:#f2433f"></div>
  <div class="swatch selected" style="left:894px;background:#8e3bd8"></div>
  <div class="swatch" style="left:928px;background:#6a3be0"></div>
  <div class="swatch" style="left:962px;background:#3d9fdb"></div>
  <div class="swatch" style="left:996px;background:#3ed1b0"></div>
  <div class="swatch" style="left:1030px;background:#d4c93a"></div>
  <div class="swatch" style="left:1064px;background:#de6b3f"></div>

  <div class="abs hrule"></div>

  <div class="label" style="left:594px;top:430px">Patch shape</div>
  <div class="shape-img straw" style="left:748px;width:46px;border-radius:50%" role="img" aria-label="Round patch"></div>
  <div class="shape-img straw" style="left:818px;width:46px" role="img" aria-label="Square patch"></div>
  <div class="shape-img straw" style="left:887px;width:68px" role="img" aria-label="Rectangle patch"></div>
  <div class="shape-img" style="left:980px;width:46px;background:#d9418d;border:3px solid #f3c4da" role="img" aria-label="Custom patch"></div>
  <div class="shape-label" style="left:748px;width:46px">Round</div>
  <div class="shape-label" style="left:808px;width:66px">Square</div>
  <div class="shape-label" style="left:881px;width:80px">Rectangle</div>
  <div class="shape-label" style="left:973px;width:60px">Custom</div>

  <div class="label" style="left:594px;top:526px">Patch location</div>
  <div class="loc" style="left:750px;width:71px">Front</div>
  <div class="loc on" style="left:827px;width:70px">Back</div>
  <div class="loc" style="left:904px;width:68px">Left</div>
  <div class="loc" style="left:980px;width:96px">Other Options</div>

  <div class="label" style="left:594px;top:592px">Quantity</div>
  <div class="abs qty"><span class="v">1</span><span class="qbtn" style="left:82px">-</span><span class="qbtn" style="left:115px">+</span></div>
  <div class="abs tiers"><span>$ 12.00 x 1</span>|<span>$ 10.00 x 10</span>|<span>$ 8.00 x 25</span></div>

  <div class="abs btn-pink" style="left:590px;top:657px;width:174px;height:54px;font-size:16px">ADD TO CART</div>
</section>

<section class="faq">
  <h2 class="abs section-title t-pink" style="top:70px">FAQ’s</h2>
  <div class="abs title-rule" style="top:145px"></div>

  <div class="faq-q" style="top:176px">Gaerspiciatis unde omnis iste natus.</div>
  <div class="faq-toggle" style="top:181px"><svg width="9" height="9" viewBox="0 0 9 9"><path d="M1.5 6l3-3 3 3" stroke="#fff" stroke-width="1.6" fill="none"/></svg></div>
  <p class="abs faq-a">Karpiciatis unde omnis iste natus error sseit voluptatem accusantium doloremque laudan seftium, tsetam aseeem aperiam, eaque ipsa quae ab illo.</p>

  <div class="faq-q" style="top:318px">Eaoluptatem accusantium antium?</div>
  <div class="faq-toggle" style="top:321px"><svg width="9" height="9" viewBox="0 0 9 9"><path d="M1.5 3l3 3 3-3" stroke="#fff" stroke-width="1.6" fill="none"/></svg></div>
  <div class="faq-q" style="top:369px">Kaerspiciatis unde omnis iste?</div>
  <div class="faq-toggle" style="top:372px"><svg width="9" height="9" viewBox="0 0 9 9"><path d="M1.5 3l3 3 3-3" stroke="#fff" stroke-width="1.6" fill="none"/></svg></div>
  <div class="faq-q" style="top:419px">Cansequuntur magni dolores?</div>
  <div class="faq-toggle" style="top:422px"><svg width="9" height="9" viewBox="0 0 9 9"><path d="M1.5 3l3 3 3-3" stroke="#fff" stroke-width="1.6" fill="none"/></svg></div>
  <div class="faq-q" style="top:470px">Vaoluptatem sequi nesciunt?</div>
  <div class="faq-toggle" style="top:472px"><svg width="9" height="9" viewBox="0 0 9 9"><path d="M1.5 3l3 3 3-3" stroke="#fff" stroke-width="1.6" fill="none"/></svg></div>
</section>

<section class="delivery">
  <h2 class="abs section-title" style="top:70px"><span class="t-gold">Delivery</span> <span class="t-pink">Status</span></h2>
  <div class="abs title-rule" style="top:143px"></div>

  <div class="step-head" style="left:94px;top:172px">Pickup Time</div>
  <div class="step-time" style="left:94px;top:197px">04:00 PM</div>
  <div class="step-head" style="left:482px;top:172px">On The Way</div>
  <div class="step-time" style="left:482px;top:197px">05:00 PM</div>
  <div class="step-head" style="left:850px;top:172px">Expected time</div>
  <div class="step-time" style="left:850px;top:197px">06:00 PM</div>

  <svg class="abs" style="left:260px;top:262px" width="660" height="120" viewBox="0 0 660 120" fill="none" stroke="#d9418d" stroke-width="1.5" stroke-dasharray="5 5">
    <path d="M10 90C80 125 180 118 290 92"/>
    <path d="M420 45C480 22 560 18 640 30"/>
  </svg>
  <div class="step-art" style="left:156px;width:120px;background:linear-gradient(180deg,#eef3f0,#dfe8e3)" role="img" aria-label="Courier collecting a parcel at a door"></div>
  <div class="step-art" style="left:500px;width:190px;background:linear-gradient(180deg,#e8f0ec,#d5e4dc)" role="img" aria-label="Green delivery van driving"></div>
  <div class="step-art" style="left:910px;width:150px;background:linear-gradient(180deg,#eef1f6,#dde4ef)" role="img" aria-label="Courier handing a parcel to a customer"></div>

  <div class="step-name t-pink" style="left:84px;top:402px">Product Pickup</div>
  <div class="step-name t-gold" style="left:472px;top:402px">On the way</div>
  <div class="step-name t-gold" style="left:848px;top:402px">Product Received</div>

  <svg class="abs" style="left:207px;top:441px" width="24" height="24" viewBox="0 0 24 24"><circle cx="12" cy="12" r="12" fill="#3ec45a"/><path d="M6.5 12.5l3.5 3.5 7.5-8" stroke="#fff" stroke-width="2.4" fill="none"/></svg>
  <svg class="abs" style="left:596px;top:441px" width="24" height="24" viewBox="0 0 24 24" fill="none" stroke="#8a8480" stroke-width="2"><circle cx="12" cy="12" r="10.5"/><path d="M6.5 12h11"/></svg>
  <svg class="abs" style="left:969px;top:441px" width="24" height="24" viewBox="0 0 24 24" fill="none" stroke="#8a8480" stroke-width="2"><circle cx="12" cy="12" r="10.5"/><path d="M6.5 12h11"/></svg>
</section>

<section class="reviews-sec">
  <h2 class="abs section-title" style="top:78px"><span class="t-pink t-italic">Our</span> <span class="t-gold">Happy Customers</span></h2>
  <div class="abs title-rule" style="top:148px"></div>

  <div class="card" style="left:-252px">
    <span class="q">”</span>
    <p>“Faerspiciatis unde omnis iste natus error sit vollsaci uptatem accusantium doloremque laudantium, totam reasciseom aperiam, eaque ipsa quae ab illo inventore veriasetatis et quasi architecto beatae vitae dicta sunt aseicse sexplicabo.”</p>
  </div>
  <div class="card" style="left:96px">
    <h3>Nadia R. Fontaine</h3>
    <div class="stars"><svg width="90" height="15" viewBox="0 0 100 18" fill="#f2d31b"><path id="t" d="M9 1l2.4 5.2 5.6.6-4.2 3.8 1.2 5.6L9 13.4 4 16.2l1.2-5.6L1 6.8l5.6-.6z"/><use href="#t" x="20"/><use href="#t" x="40"/><use href="#t" x="60"/><use href="#t" x="80"/></svg></div>
    <span class="q">”</span>
    <p>“Faerspiciatis unde omnis iste natus error sit vollsaci uptatem accusantium doloremque laudantium, totam reasciseom aperiam, eaque ipsa quae ab illo inventore veriasetatis et quasi architecto beatae vitae dicta sunt aseicse sexplicabo.”</p>
  </div>
  <div class="card" style="left:444px">
    <h3>Lena M. Okafor</h3>
    <div class="stars"><svg width="90" height="15" viewBox="0 0 100 18" fill="#f2d31b"><use href="#t"/><use href="#t" x="20"/><use href="#t" x="40"/><use href="#t" x="60"/><use href="#t" x="80"/></svg></div>
    <span class="q">”</span>
    <p>“Faerspiciatis unde omnis iste natus error sit vollsaci uptatem accusantium doloremque laudantium, totam reasciseom aperiam, eaque ipsa quae ab illo inventore veriasetatis et quasi architecto beatae vitae dicta sunt aseicse sexplicabo.”</p>
  </div>
  <div class="card" style="left:790px">
    <h3>Thomas E. Ravel</h3>
    <div class="stars"><svg width="90" height="15" viewBox="0 0 100 18" fill="#f2d31b"><use href="#t"/><use href="#t" x="20"/><use href="#t" x="40"/><use href="#t" x="60"/><use href="#t" x="80"/></svg></div>
    <span class="q">”</span>
    <p>“Faerspiciatis unde omnis iste natus error sit vollsaci uptatem accusantium doloremque laudantium, totam reasciseom aperiam, eaque ipsa quae ab illo inventore veriasetatis et quasi architecto beatae vitae dicta sunt aseicse sexplicabo.”</p>
  </div>
  <div class="card" style="left:1138px">
    <h3>Mia</h3>
    <div class="stars"><svg width="90" height="15" viewBox="0 0 100 18" fill="#f2d31b"><use href="#t"/><use href="#t" x="20"/><use href="#t" x="40"/><use href="#t" x="60"/><use href="#t" x="80"/></svg></div>
    <p>“Faerspiciatis unde omnis iste natus error sit vollsaci uptatem accusantium doloremque laudantium, totam reasciseom aperiam, eaque ipsa quae ab illo inventore veriasetatis et quasi architecto beatae vitae dicta sunt aseicse sexplicabo.”</p>
  </div>

  <span class="rdot" style="left:590px"></span>
  <span class="rdot" style="left:613px"></span>
  <span class="rdot on" style="left:636px"></span>
</section>

<section class="newsletter">
  <h2 class="abs section-title" style="top:64px"><span class="t-pink t-italic">Subscribe To</span> <span class="t-gold">Join Our Newsletter</span></h2>
  <p class="abs nl-sub">Sed ut perspiciatis unde omnis iste natus error sit voluptatem accusantium</p>
  <div class="abs nl-input"><svg width="12" height="10" viewBox="0 0 12 10"><rect width="12" height="10" rx="1" fill="#6b625c"/><path d="M0.5 1l5.5 4 5.5-4" stroke="#fff" stroke-width="1" fill="none"/></svg>Email Address</div>
  <div class="abs btn-pink" style="left:728px;top:179px;width:152px;height:41px;font-size:14px">SUBSCRIBE</div>
</section>

<footer class="site-footer">
  <div class="abs f-brand">Brimcraft</div>
  <span class="social" style="left:140px" aria-label="Social profile"></span>
  <span class="social" style="left:205px" aria-label="Messaging"></span>
  <span class="social" style="left:270px" aria-label="Photo profile"></span>

  <div class="f-head" style="left:376px">MAIN LINKS</div>
  <div class="f-link" style="top:130px">Home</div>
  <div class="f-link" style="top:160px">About Us</div>
  <div class="f-link" style="top:190px">Our Product</div>
  <div class="f-link" style="top:221px">Blog</div>
  <div class="f-link" style="top:250px">Contact</div>

  <div class="f-head" style="left:560px">CONTACT US</div>
  <svg class="f-icon" style="top:134px" width="15" height="15" viewBox="0 0 16 16"><path d="M3.6 1l2.6 3-1.6 2a9 9 0 0 0 4.8 4.8l2-1.6 3 2.6-1.6 2.6C7.6 14.6 1.4 8.4 1 2.6z" fill="#1f1a17"/></svg>
  <div class="f-contact" style="top:126px">+1 555 014 2200</div>
  <svg class="f-icon" style="top:164px" width="14" height="17" viewBox="0 0 14 18"><path d="M7 0a6.5 6.5 0 0 0-6.5 6.5C.5 11.4 7 18 7 18s6.5-6.6 6.5-11.5A6.5 6.5 0 0 0 7 0zm0 9a2.5 2.5 0 1 1 0-5 2.5 2.5 0 0 1 0 5z" fill="#1f1a17"/></svg>
  <div class="f-contact" style="top:158px">Lorem Ipsum is simply<br>dummy text of the printing</div>
  <svg class="f-icon" style="top:233px" width="15" height="11" viewBox="0 0 15 11"><rect width="15" height="11" rx="1" fill="#1f1a17"/><path d="M.8 1l6.7 5 6.7-5" stroke="#e8ad98" stroke-width="1.2" fill="none"/></svg>
  <div class="f-contact" style="top:222px">hello@brimcraft.shop</div>

  <div class="f-head" style="left:858px">NEWSLETTER SIGN UP</div>
  <p class="abs f-note">We Will Notify You Of Any Important News</p>
  <div class="abs f-input">Your Email Address</div>
  <div class="abs f-send"><svg style="position:absolute;left:13px;top:10px" width="22" height="22" viewBox="0 0 24 24" fill="none" stroke="#fff" stroke-width="1.6"><path d="M22 2L11 13"/><path d="M22 2l-7 20-4-9-9-4z"/></svg></div>

  <div class="abs f-rule"></div>
  <p class="abs copyright">© 2025 brimcraft I All Rights Reserved</p>
</footer>

</body>
</html>
```